Supplement Label Design for “Kelvora Gut” – Premium Bilingual Supplement

Kelvora is a premium, individually crafted supplement brand specializing in targeted solutions for specific health issues.
We are launching our first product: Kelvora Gut — a high-quality blend focused on stomach and digestive health.
Primary goals:
• Reduce symptoms caused by Helicobacter pylori (acidity after meals, stomach pain and discomfort)
• Support repair of the gut lining
• Strengthen the local immune system in the digestive tract
Label Requirements:
• Premium, elegant, and modern design (high-end supplement feel)
• Dominant yellow / golden color scheme for this Gut blend (future blends will have different signature colors, e.g. red for Heart blend)
• Include a stylized, positive illustration of a healthy stomach on the label
• Fully bilingual — English and Bulgarian if possible (both languages must be clearly visible and well balanced)
• Logo is already uploaded
• Must feel trustworthy, clean, and professional
We need both front and back label designs suitable for a standard supplement bottle.

Target Market(s)

The target is health-conscious individuals, particularly my personal patients who suffer from stomach issues, H. pylori related symptoms, and digestive discomfort. People looking for premium, science-oriented natural supplements.

Industry/Entity Type

Functional medicine

Font styles to use
Sans Serif

Colors
FFC000
F8CF3A
FAE287
FDF2CF
FEFAEE

Requirements
Must have
• • Premium and luxurious look • Dominant yellow/golden color palette • Stylized healthy stomach illustration • Bilingual (English + Bulgarian) • Clean, minimalist yet elegant design • Professional and trustworthy appearance • Include the “Kelvora” logo
Nice to have
• • Subtle visual indication of positive effect on the stomach/gut • Elegant iconography or subtle patterns related to health and nature • Easy-to-read hierarchy for important information • Modern minimalist style with premium finishing feel
Should not have
• Cheap or generic look • Overly cartoonish or childish stomach drawing • Too much clutter or overcrowded desig

```html
<!DOCTYPE html>
<html lang="en">
<head>
<meta charset="utf-8">
<title>Kelvora Gut – Front Label</title>
<link rel="stylesheet" href="https://fonts.googleapis.com/css2?family=Playfair+Display:wght@800&family=Roboto:wght@500;700&display=swap">
<style>
  :root {
    --gold-deep: #FFC000;
    --gold: #F8CF3A;
    --gold-soft: #FAE287;
    --cream: #FDF2CF;
    --ivory: #FEFAEE;
    --ink: #262626;
    --ink-soft: #5a5a5a;
    --rule: rgba(170, 130, 40, 0.35);
    --page: #ffffff;
  }
  * { box-sizing: border-box; margin: 0; padding: 0; }
  html, body { width: 1200px; height: 1200px; overflow: hidden; background: var(--page); }
  .canvas { position: relative; width: 1200px; height: 1200px; }

  .label {
    position: absolute; left: 190px; top: 62px; width: 820px; height: 1076px;
    background: linear-gradient(180deg, var(--ivory) 0%, var(--cream) 30%, var(--gold-soft) 70%, var(--gold) 100%);
    overflow: hidden;
    font-family: "Roboto", Arial, sans-serif;
    text-align: center;
  }

  .brand {
    position: absolute; top: 92px; left: 0; right: 0;
    display: flex; justify-content: center; align-items: center; gap: 12px;
  }
  .brand-name {
    font-family: "Roboto", Arial, sans-serif; font-weight: 500;
    font-size: 40px; letter-spacing: 1px; color: var(--ink-soft);
  }
  .brand-dot { width: 10px; height: 10px; border-radius: 50%; background: var(--ink-soft); }

  .product-name {
    position: absolute; top: 165px; left: 0; right: 0;
    font-family: "Playfair Display", Georgia, serif; font-weight: 800;
    font-size: 270px; line-height: 1; letter-spacing: 6px; color: var(--ink);
  }

  .subtitle {
    position: absolute; left: 0; right: 0;
    font-weight: 700; font-size: 29px; letter-spacing: 2.5px; color: var(--ink-soft);
  }
  .subtitle strong { color: var(--ink); }
  .subtitle.en { top: 440px; }
  .subtitle.bg { top: 487px; font-weight: 500; letter-spacing: 2px; }

  .illustration {
    position: absolute; left: 170px; top: 530px; width: 500px; height: 345px;
    border-radius: 48% 52% 46% 54% / 40% 45% 55% 60%;
    background: radial-gradient(ellipse at 55% 45%, #fff1b0 0%, var(--gold-deep) 45%, rgba(230,160,20,0.55) 75%, rgba(248,207,58,0) 100%);
  }

  .badge {
    position: absolute; left: 185px; top: 585px; width: 150px; height: 150px;
    border-radius: 50%; background: rgba(230, 150, 20, 0.45);
    border: 3px solid rgba(255, 240, 200, 0.8);
    display: flex; flex-direction: column; justify-content: center; align-items: center;
    font-weight: 700; font-size: 11px; letter-spacing: 1px; line-height: 1.5; color: #fff8e6;
  }

  .tagline {
    position: absolute; left: 40px; right: 40px; top: 880px;
    border-top: 2px solid var(--rule); padding-top: 20px;
  }
  .tagline p { font-weight: 700; font-size: 25px; letter-spacing: 2px; color: var(--ink-soft); line-height: 34px; }
  .tagline p.bg { font-weight: 500; color: rgba(90, 80, 60, 0.7); }

  .footer-band {
    position: absolute; left: 40px; right: 40px; top: 972px; bottom: 0;
    border-top: 2px solid var(--rule);
    display: grid; grid-template-columns: 383px 1fr;
  }
  .footer-band .col {
    padding-top: 22px; font-weight: 700; font-size: 22px; letter-spacing: 2px; line-height: 32px; color: var(--ink-soft);
  }
  .footer-band .col.en { text-align: right; padding-right: 22px; border-right: 2px solid var(--rule); }
  .footer-band .col.bg { text-align: left; padding-left: 22px; color: rgba(120, 85, 20, 0.8); }
</style>
</head>
<body>
<div class="canvas">
  <section class="label">
    <div class="brand">
      <span class="brand-name">Kelvora</span>
      <span class="brand-dot"></span>
    </div>

    <h1 class="product-name">GUT</h1>

    <p class="subtitle en">STOMACH &amp; <strong>DIGESTIVE HEALTH</strong></p>
    <p class="subtitle bg">СТОМАШНО-ЧРЕВНО ЗДРАВЕ</p>

    <div class="illustration" role="img" aria-label="Stylized glowing golden illustration of a healthy stomach with soft sparkles"></div>

    <div class="badge">
      <span>HELPS REDUCE</span>
      <span>SYMPTOMS</span>
      <span>CAUSED BY</span>
      <span>PYLORI</span>
    </div>

    <div class="tagline">
      <p class="en">TARGETED RELIEF, LASTING COMFORT.</p>
      <p class="bg">БЪРЗО ОБЛЕКЧЕНИЕ. ДЪЛЪГ КОМФОРТ.</p>
    </div>

    <div class="footer-band">
      <div class="col en">DIETARY SUPPLEMENT<br>60 CAPSULES</div>
      <div class="col bg">ХРАНИТЕЛНА ДОБАВКА<br>60 КАПСУЛИ</div>
    </div>
  </section>
</div>
</body>
</html>
```